A Healthy QORV Louisiana- TBLW Conference Poster

LA Carewell is presenting at the TBLW conference. The TBLW is a annual meeting for State, Federal and private sector individuals to provide opportunities for the exchange of ideas related to Carewell systems and heath policy affected by those systems. Louisiana will be presenting on their LaQORV Program . A poster with the information in the PowerPoint is needed. The first slide shows a draft of organization. The wording on slides two and three should be displayed in a visually appealing infographic. The charts should coordinate with the overall design. We would like to see the Louisiana state capital building incorporated.

Font styles to use
Sans Serif

Colors

Designer to choose colors to be used in the design.

Requirements
Must have
• Visually appealing infographics and charts
Nice to have
• Incorporate the capital building, incorporate the LaQORV logo (on first slide)

```html
<!DOCTYPE html>
<html lang="en">
<head>
<meta charset="utf-8">
<title>A Healthy QORV Louisiana</title>
<link rel="stylesheet" href="https://fonts.googleapis.com/css2?family=Lato:wght@400;700;900&family=Tinos:wght@400;700&family=Roboto+Slab:wght@500&display=swap">
<style>
  :root {
    --ink-dark: #141414;
    --dusk-purple: #8c70b8;
    --dusk-violet: #5b3f86;
    --obstacle-red: #ff5a5a;
    --solution-green: #3fd23f;
    --chart-red: #ff5f5f;
    --chart-green: #44e044;
    --white: #ffffff;
    --body-text: #f4f0f8;
  }
  * { box-sizing: border-box; margin: 0; padding: 0; }
  html, body { width: 1200px; height: 580px; overflow: hidden; background: var(--ink-dark); }
  .poster {
    position: relative; width: 1200px; height: 580px; overflow: hidden;
    font-family: "Tinos", "Times New Roman", serif; color: var(--white);
  }
  .capitol-scene {
    position: absolute; inset: 0;
    background:
      radial-gradient(ellipse 160px 300px at 600px 330px, rgba(40,28,60,0.55), transparent 70%),
      linear-gradient(90deg, #0d0d0f 0%, #2b2238 28%, #6a5090 55%, var(--dusk-purple) 78%, #9a86c4 100%);
  }
  .capitol-scene::after {
    content: ""; position: absolute; left: 0; right: 0; bottom: 0; height: 150px;
    background: linear-gradient(180deg, transparent, rgba(10,8,16,0.75));
  }
  .title {
    position: absolute; left: 60px; top: 42px;
    font-family: "Lato", sans-serif; font-weight: 700; font-size: 42px; letter-spacing: 0.3px;
  }
  .intro {
    position: absolute; left: 680px; top: 20px; width: 505px;
    font-size: 11.4px; font-weight: 700; line-height: 1.36; text-align: justify; color: var(--body-text);
  }
  .intro p + p { margin-top: 13px; }
  .card {
    position: absolute; border: 1.5px solid; border-radius: 14px;
    border-bottom-color: transparent !important; border-left-color: transparent !important;
  }
  .card--obstacle { border-color: rgba(255,90,90,0.6); }
  .card--solution { border-color: rgba(63,210,63,0.6); }
  .pill {
    position: absolute; display: flex; align-items: center; justify-content: center; text-align: center;
    font-family: "Lato", sans-serif; font-weight: 700; font-size: 12.5px; line-height: 1.15;
    border-radius: 22px; text-transform: uppercase;
  }
  .pill--obstacle { background: var(--obstacle-red); color: var(--white); }
  .pill--solution { background: var(--solution-green); color: var(--white); }
  .card-text {
    position: absolute; font-size: 9.4px; font-weight: 700; line-height: 1.32;
    text-align: justify; color: var(--body-text);
  }
  .section-banner {
    position: absolute; top: 122px; width: 60px; height: 284px; border-radius: 30px;
    display: flex; align-items: center; justify-content: center;
    box-shadow: 0 0 0 3px rgba(255,255,255,0.15);
  }
  .section-banner span {
    writing-mode: vertical-rl; font-family: "Roboto Slab", serif; font-weight: 500;
    font-size: 27px; letter-spacing: 1px; color: var(--white);
  }
  .section-banner--obstacles { left: 483px; background: var(--obstacle-red); }
  .section-banner--solutions { left: 663px; background: var(--solution-green); }
  .chart { position: absolute; left: 0; top: 0; }
  .chart text { font-family: "Lato", sans-serif; font-weight: 700; font-size: 10px; }
  .program-mark {
    position: absolute; left: 566px; top: 544px; width: 84px; height: 38px;
    background: var(--white); border-radius: 4px;
    display: flex; align-items: center; justify-content: center; gap: 5px;
    font-family: "Lato", sans-serif; font-weight: 700; font-size: 13px; color: #2e6ea6;
  }
  .program-mark i { width: 10px; height: 10px; background: #2e6ea6; display: block; }
</style>
</head>
<body>
<main class="poster">
  <div class="capitol-scene" role="img" aria-label="Louisiana State Capitol tower at dusk under a purple sky with trees in the foreground"></div>

  <h1 class="title">A Healthy QORV Louisiana</h1>

  <section class="intro">
    <p>Louisiana Quality Options Reimbursement Venture (LaQORV) program allows for Carewell to pay the premium costs of member's private health insurance when cost effective for the State.</p>
    <p>To increase program participation the State is implementing strategic changes to increase enrollment by 95%, resulting in an $11.2M cost savings to the State by the end of SFY23.</p>
  </section>

  <!-- Obstacles -->
  <div class="card card--obstacle" style="left:52px;top:163px;width:182px;height:102px"></div>
  <div class="pill pill--obstacle" style="left:65px;top:136px;width:156px;height:50px">Lack of<br>Public Knowledge</div>
  <p class="card-text" style="left:62px;top:203px;width:165px">Members are unaware that this program exists or find it hard to believe that Carewell will pay for their private health insurance.</p>

  <div class="card card--obstacle" style="left:285px;top:163px;width:180px;height:100px"></div>
  <div class="pill pill--obstacle" style="left:290px;top:150px;width:168px;height:26px">Budget Constraints</div>
  <p class="card-text" style="left:293px;top:182px;width:165px">Due to a budgetary shortfall the LaQORV program was discontinued on Dec 2015. By ending the program, all members were forced to cover their private insurance premiums, or switch to Carewell.</p>

  <div class="card card--obstacle" style="left:52px;top:305px;width:182px;height:100px"></div>
  <div class="pill pill--obstacle" style="left:82px;top:282px;width:124px;height:50px">Lack of<br>Participation</div>
  <p class="card-text" style="left:62px;top:343px;width:165px">Cost effectiveness formula is too restrictive excluding a large portion of the viable population, including waiver, Fee for Service (FFS) members and the individual insurance market.</p>

  <div class="card card--obstacle" style="left:288px;top:305px;width:178px;height:90px"></div>
  <div class="pill pill--obstacle" style="left:328px;top:291px;width:96px;height:26px">Crowd Out</div>
  <p class="card-text" style="left:296px;top:338px;width:163px">Crowd out occurs when members choose public insurance in lieu of available private health insurance.</p>

  <div class="section-banner section-banner--obstacles"><span>THE OBSTACLES</span></div>
  <div class="section-banner section-banner--solutions"><span>THE SOLUTIONS</span></div>

  <!-- Solutions -->
  <div class="card card--solution" style="left:770px;top:160px;width:175px;height:100px"></div>
  <div class="pill pill--solution" style="left:783px;top:147px;width:146px;height:26px">Program Restored</div>
  <p class="card-text" style="left:778px;top:196px;width:164px">LaQORV was reinstated in April 2017, restoring LCD's focus on promoting employer-sponsored insurance.</p>

  <div class="card card--solution" style="left:1002px;top:160px;width:176px;height:100px"></div>
  <div class="pill pill--solution" style="left:1010px;top:146px;width:154px;height:38px">Increase Awareness<br>&amp; Public Knowledge</div>
  <p class="card-text" style="left:1010px;top:190px;width:163px">LCD has contracted a marketing firm to develop a comprehensive marketing and outreach strategy aimed at engaging providers, employers, insurance companies and members.</p>

  <div class="card card--solution" style="left:770px;top:305px;width:176px;height:98px"></div>
  <div class="pill pill--solution" style="left:780px;top:287px;width:150px;height:40px">Increase<br>Participation</div>
  <p class="card-text" style="left:778px;top:330px;width:164px">Refinement of the cost effectiveness formula increased the pool of members eligible for the program, including waiver, Fee for Service (FFS) members and the individual insurance market.</p>

  <div class="card card--solution" style="left:1002px;top:305px;width:176px;height:90px"></div>
  <div class="pill pill--solution" style="left:1014px;top:288px;width:146px;height:24px">Data &amp; Analytics</div>
  <p class="card-text" style="left:1010px;top:336px;width:163px">The use of data mining identifies individuals and populations to be targeted for program outreach.</p>

  <!-- Charts -->
  <svg class="chart" width="1200" height="580" viewBox="0 0 1200 580" aria-label="Participant charts">
    <g class="chart-participants-before" stroke="var(--chart-red)" fill="var(--chart-red)">
      <line x1="88" y1="556" x2="392" y2="556" stroke-width="2"/>
      <g stroke-dasharray="4 3" stroke-width="1.2">
        <line x1="177" y1="512" x2="177" y2="556"/>
        <line x1="240" y1="467" x2="240" y2="556"/>
        <line x1="304" y1="423" x2="304" y2="556"/>
      </g>
      <polyline points="114,556 177,512 240,467 304,423 367,556" fill="none" stroke-width="2"/>
      <g stroke="none">
        <circle cx="114" cy="556" r="3.5"/><circle cx="177" cy="512" r="3.5"/><circle cx="240" cy="467" r="3.5"/>
        <circle cx="304" cy="423" r="3.5"/><circle cx="367" cy="556" r="3.5"/>
        <circle cx="177" cy="556" r="3"/><circle cx="240" cy="556" r="3"/><circle cx="304" cy="556" r="3"/>
      </g>
      <line x1="306" y1="425" x2="332" y2="440" stroke-width="1"/>
      <g stroke="none" text-anchor="middle">
        <text x="114" y="549">0</text><text x="177" y="505">500</text><text x="240" y="460">1000</text>
        <text x="304" y="416">1500</text><text x="367" y="549">0</text>
        <text x="114" y="573">FY12</text><text x="177" y="573">FY13</text><text x="240" y="573">FY14</text>
        <text x="304" y="573">FY15</text><text x="367" y="573">FY16</text>
        <text x="360" y="444" font-weight="400" font-size="9.5">Funding Lost</text>
        <text x="240" y="588">LaQORV Participants Chart</text>
      </g>
    </g>

    <g class="chart-participants-after" stroke="var(--chart-green)" fill="var(--chart-green)">
      <line x1="815" y1="556" x2="1112" y2="556" stroke-width="2"/>
      <g stroke-dasharray="4 3" stroke-width="1.2">
        <line x1="883" y1="516" x2="883" y2="556"/>
        <line x1="935" y1="504" x2="935" y2="556"/>
        <line x1="987" y1="479" x2="987" y2="556"/>
        <line x1="1037" y1="455" x2="1037" y2="556"/>
        <line x1="1089" y1="425" x2="1089" y2="556"/>
      </g>
      <polyline points="831,556 883,516 935,504 987,479 1037,455 1089,425" fill="none" stroke-width="2"/>
      <g stroke="none">
        <circle cx="831" cy="556" r="3.5"/><circle cx="883" cy="516" r="3.5"/><circle cx="935" cy="504" r="3.5"/>
        <circle cx="987" cy="479" r="3.5"/><circle cx="1037" cy="455" r="3.5"/><circle cx="1089" cy="425" r="3.5"/>
        <circle cx="883" cy="556" r="3"/><circle cx="935" cy="556" r="3"/><circle cx="987" cy="556" r="3"/>
        <circle cx="1037" cy="556" r="3"/><circle cx="1089" cy="556" r="3"/>
      </g>
      <g stroke-width="1">
        <line x1="800" y1="528" x2="829" y2="554"/>
        <line x1="860" y1="488" x2="881" y2="514"/>
        <line x1="860" y1="455" x2="933" y2="502"/>
        <line x1="937" y1="506" x2="952" y2="515"/>
      </g>
      <g stroke="none" text-anchor="middle">
        <text x="831" y="544">0</text><text x="889" y="510">435</text><text x="935" y="496">566</text>
        <text x="987" y="471">848</text><text x="1037" y="447">1103</text><text x="1089" y="415">1434</text>
        <text x="831" y="573">FY17</text><text x="883" y="573">FY19</text><text x="935" y="573">FY20</text>
        <text x="987" y="573">FY21</text><text x="1037" y="573">FY22</text><text x="1089" y="573">FY23</text>
        <text x="780" y="526" font-weight="400">Program Restored</text>
        <text x="852" y="487" font-weight="400">Current</text>
        <text x="830" y="441" font-weight="400">Marketing Firm</text>
        <text x="830" y="454" font-weight="400">Engaged</text>
        <text x="963" y="522" font-weight="400">Formula</text>
        <text x="963" y="535" font-weight="400">Refined</text>
      </g>
    </g>
  </svg>

  <div class="program-mark"><i></i>LaQORV</div>
</main>
</body>
</html>
```